Keelby marketing postcards (6x9)

I would like to replicate this 6x9 postcard, but update name/logo, phone number, web address, etc. I also need to create a second postcard copying this basic design, but with updated content and background pictures. Updated contact info to be used for both postcards:
Website: www.keelbyhomestay.com
Name: Mark Tessler
Email: mtessler@keelbyhomestay.com
Phone: (555) 246-8130

Requirements
Must have
• Need two 6x9 postcard designs; 1 themed for Rivenport College, 1 for Calder State. Have uploaded photos that can be used in design. RC can be used for RC postcard (only), CS can be used for CS (only), Generic can be used for either. I've tried to upload extra photos so that you can use your creativity in selecting those that work best in the design.
Nice to have
• In the "Color palette" file, it has the two color schemes -- one for Rivenport College and one for Calder State. Those respective color schemes should be heavily represented in each design. Then there are different groups of pictures labelled either "CS" or "RC", plus some labelled "Generic". The generic ones can be used in either design, the others should be used only for the design for that school.

```html
<!DOCTYPE html>
<html lang="en">
<head>
<meta charset="utf-8">
<title>Keelby Homestay postcards</title>
<link rel="stylesheet" href="https://fonts.googleapis.com/css2?family=Open+Sans:wght@400;600;700&family=Oswald:wght@400;500&display=swap">
<style>
:root{
  --stage:#c9c9c9;
  --ink:#111;
  --navy:#1a2033;
  --orange:#e0701e;
  --orange-dark:#b0531a;
  --maroon:#6d1435;
  --maroon-dark:#561029;
  --cocoa:#2a1511;
  --logo-blue:#5fb2d8;
  --white:#fff;
  --rule:#bfbfbf;
}
*{box-sizing:border-box;margin:0;padding:0}
html,body{width:1200px;height:873px;overflow:hidden}
body{background:var(--stage);font-family:"Open Sans",sans-serif;position:relative;color:var(--ink)}
.set-label{position:absolute;font-family:"Open Sans",sans-serif;font-weight:700;font-size:26px;letter-spacing:-.2px;color:#0d0d0d}
.card{position:absolute;width:441px;height:297px;overflow:hidden;box-shadow:0 3px 8px rgba(0,0,0,.35)}

/* front */
.front{color:var(--white)}
.front--rc{background:var(--navy)}
.front--cs{background:var(--cocoa)}
.front .photo{position:absolute;top:0;right:0;width:260px;height:100%;
  -webkit-mask-image:linear-gradient(90deg,transparent 0,#000 40%);mask-image:linear-gradient(90deg,transparent 0,#000 40%)}
.front--rc .photo{background:linear-gradient(180deg,#3f86c8 0%,#8fbde0 30%,#d8cdb2 55%,#4d7a35 75%,#2c4a22 100%)}
.front--cs .photo{background:linear-gradient(180deg,#5c3b5e 0%,#d36a4f 35%,#e9a45a 50%,#3a2a3c 70%,#15101a 100%)}
.front .brand{position:absolute;left:20px;top:40px;font-family:"Oswald",sans-serif;font-weight:500;font-size:23px;color:var(--logo-blue);text-transform:uppercase;display:flex;align-items:center;gap:8px}
.front .brand .mark{width:14px;height:14px;background:var(--logo-blue)}
.front .audience{position:absolute;left:19px;top:106px;font-weight:700;font-size:12px;text-transform:uppercase}
.front .headline{position:absolute;left:0;top:129px;width:280px;height:64px;padding:8px 0 0 17px;font-weight:600;font-size:21px;line-height:27px;text-transform:uppercase}
.front--rc .headline{background:var(--orange)}
.front--cs .headline{background:var(--maroon);width:295px}
.front .lede{position:absolute;left:18px;top:204px;width:225px;font-size:7.6px;line-height:10px;font-weight:600}
.front .saving{position:absolute;left:18px;top:234px;font-size:8.6px;font-weight:600}
.front .baseline{position:absolute;left:0;right:0;top:274px;height:1px;background:var(--white)}
.front .url-pill{position:absolute;left:136px;top:267px;width:177px;height:15px;border:1px solid var(--white);border-radius:8px;font-size:8.4px;font-weight:700;letter-spacing:1.5px;text-align:center;line-height:13px}
.front--rc .url-pill{background:var(--orange)}
.front--cs .url-pill{background:var(--cocoa)}

/* back */
.back{background:var(--white)}
.back .grid{position:absolute;left:0;top:0;width:225px;height:235px}
.back .cell{position:absolute;color:var(--white)}
.back .intro{left:0;top:0;width:118px;height:80px;padding:16px 6px 0 17px;font-size:6.6px;line-height:9px;font-weight:600}
.back .intro small{display:block;margin-top:3px;font-size:5.8px;line-height:8px}
.back .strip{left:118px;top:0;width:107px;height:16px}
.back .photo-a{left:118px;top:16px;width:107px;height:64px}
.back .photo-b{left:0;top:81px;width:117px;height:62px}
.back .cta{left:118px;top:81px;width:107px;height:62px;padding:12px 4px 0 8px;font-size:5.8px;line-height:8px;font-weight:600}
.back .cta span{display:block;margin-top:5px;font-size:9.5px;font-weight:400}
.back .photo-c{left:0;top:144px;width:225px;height:91px}
.back .contact-bar{position:absolute;left:0;top:235px;width:225px;height:16px;padding:4px 0 0 20px;font-size:6.8px;font-weight:700;color:var(--white)}
.back .person{position:absolute;left:22px;top:255px;font-size:8.6px;font-weight:700}
.back .phone{position:absolute;left:20px;top:266px;font-family:"Oswald",sans-serif;font-size:11.5px;display:flex;align-items:center;gap:3px}
.back .divider{position:absolute;left:113px;top:256px;width:1px;height:24px;background:var(--navy)}
.back .links{position:absolute;left:122px;top:259px;font-size:6px;line-height:10px}
.back .links li{list-style:none;display:flex;align-items:center;gap:4px}
.back .links i{display:inline-block;width:4px;height:4px;background:#444;border-radius:1px}
.back .brand-small{position:absolute;left:238px;top:26px;font-family:"Oswald",sans-serif;font-weight:500;font-size:10px;color:var(--logo-blue);text-transform:uppercase;display:flex;align-items:center;gap:5px}
.back .brand-small .mark{width:8px;height:8px;background:var(--logo-blue)}
.back .addr{position:absolute;left:236px;top:53px;width:94px;font-size:6.6px;text-align:center;line-height:9px;border-top:1px dotted #999;padding-top:1px}
.back .addr span{display:block;border-top:1px solid #777}
.back .stamp{position:absolute;left:376px;top:16px;width:48px;height:45px;border:1px solid #666}
.back .line{position:absolute;left:249px;width:176px;height:1px;background:var(--rule)}

.back--rc .intro,.back--rc .strip,.back--rc .cta{background:var(--orange)}
.back--rc .contact-bar{background:var(--orange-dark)}
.back--rc .photo-a{background:linear-gradient(180deg,#88b7dc,#b9a27f 55%,#3f6b2e)}
.back--rc .photo-b{background:linear-gradient(180deg,#7fa8cf,#4b6a7a 50%,#2d4a2a)}
.back--rc .photo-c{background:radial-gradient(circle at 40% 60%,#d9403a 0,#2b3f8f 12%,#e4a64a 22%,#c98628 100%)}
.back--cs .intro,.back--cs .strip,.back--cs .cta{background:var(--maroon)}
.back--cs .contact-bar{background:var(--maroon-dark)}
.back--cs .photo-a{background:linear-gradient(180deg,#cfd3d8,#8fa6c4 50%,#e9e6e2)}
.back--cs .photo-b{background:linear-gradient(180deg,#e9e4dc,#b9b2a6 60%,#6a6058)}
.back--cs .photo-c{background:radial-gradient(circle at 50% 50%,#4b3aa8 0,#231a55 45%,#120d25 100%)}
</style>
</head>
<body>

<p class="set-label" style="left:145px;top:32px">RIVENPORT COLLEGE FAMILIES</p>
<p class="set-label" style="left:168px;top:818px">CALDER STATE FAMILIES</p>

<!-- Rivenport College front -->
<section class="card front front--rc" style="left:114px;top:96px">
  <div class="photo" role="img" aria-label="Domed capitol building framed by trees under a blue sky"></div>
  <div class="brand"><span class="mark"></span>Keelby Homestay</div>
  <p class="audience">Riverhawk Families</p>
  <h2 class="headline">What would you do<br>with an extra $80,000?</h2>
  <p class="lede">The professionals at Keelby Homestay are passionate about helping out-of-state families establish Texas residency and qualify for in-state tuition.</p>
  <p class="saving">Saving your family more than $13,700 per semester.</p>
  <div class="baseline"></div>
  <div class="url-pill">www.keelbyhomestay.com</div>
</section>

<!-- Rivenport College back -->
<section class="card back back--rc" style="left:658px;top:96px">
  <div class="grid">
    <div class="cell intro">Let us help you save tens of thousands of dollars on tuition in Texas.<small>Establishing Texas residency through a property purchase is as easy as 1-2-3.</small></div>
    <div class="cell strip"></div>
    <div class="cell photo-a" role="img" aria-label="Campus tower seen across a green lawn"></div>
    <div class="cell photo-b" role="img" aria-label="Arched bridge over a river in hill country"></div>
    <div class="cell cta">Contact us now to learn how Keelby Homestay is ready to become your trusted partner.<span>Let us help you too!</span></div>
    <div class="cell photo-c" role="img" aria-label="Map of the United States with Texas highlighted in flag colours"></div>
  </div>
  <div class="contact-bar">CONTACT US :</div>
  <p class="person">Mark Tessler</p>
  <p class="phone"><svg width="9" height="9" viewBox="0 0 10 10"><circle cx="5" cy="5" r="4.3" fill="none" stroke="#111" stroke-width="1"/><path d="M3.4 2.8l1 1-.5.6c.3.6.8 1.1 1.4 1.4l.6-.5 1 1-.7.8C4.6 6.8 3.2 5.4 2.6 3.5z" fill="#111"/></svg>(555) 246-8130</p>
  <div class="divider"></div>
  <ul class="links"><li><i></i>mtessler@keelbyhomestay.com</li><li><i style="border-radius:50%"></i>www.keelbyhomestay.com</li></ul>
  <div class="brand-small"><span class="mark"></span>Keelby Homestay</div>
  <p class="addr">www.keelbyhomestay.com<span>(555) 246-8130</span></p>
  <div class="stamp"></div>
  <div class="line" style="top:174px"></div>
  <div class="line" style="top:203px"></div>
  <div class="line" style="top:233px"></div>
</section>

<!-- Calder State front -->
<section class="card front front--cs" style="left:114px;top:452px">
  <div class="photo" role="img" aria-label="Illuminated clock tower at sunset over a campus"></div>
  <div class="brand" style="top:44px"><span class="mark"></span>Keelby Homestay</div>
  <p class="audience">Calder Families</p>
  <h2 class="headline">What would you do<br>with an extra $79,000?</h2>
  <p class="lede">The professionals at Keelby Homestay are passionate about helping out-of-state families establish Texas residency and qualify for in-state tuition.</p>
  <p class="saving">Saving your family more than $13,200 per semester.</p>
  <div class="baseline"></div>
  <div class="url-pill">www.keelbyhomestay.com</div>
</section>

<!-- Calder State back -->
<section class="card back back--cs" style="left:658px;top:439px">
  <div class="grid">
    <div class="cell intro">Let us help you save tens of thousands of dollars on tuition in Texas.<small>Establishing Texas residency through a property purchase is as easy as 1-2-3.</small></div>
    <div class="cell strip"></div>
    <div class="cell photo-a" role="img" aria-label="Student in a denim jacket carrying books"></div>
    <div class="cell photo-b" role="img" aria-label="Water tower reading Welcome to Calder Hill"></div>
    <div class="cell cta">Contact us now to learn how Keelby Homestay is ready to become your trusted partner.<span>Let us help you too!</span></div>
    <div class="cell photo-c" role="img" aria-label="Neon sign reading Deep in the Heart inside a Texas outline"></div>
  </div>
  <div class="contact-bar">CONTACT US :</div>
  <p class="person">Mark Tessler</p>
  <p class="phone"><svg width="9" height="9" viewBox="0 0 10 10"><circle cx="5" cy="5" r="4.3" fill="none" stroke="#111" stroke-width="1"/><path d="M3.4 2.8l1 1-.5.6c.3.6.8 1.1 1.4 1.4l.6-.5 1 1-.7.8C4.6 6.8 3.2 5.4 2.6 3.5z" fill="#111"/></svg>(555) 246-8130</p>
  <div class="divider"></div>
  <ul class="links"><li><i></i>mtessler@keelbyhomestay.com</li><li><i style="border-radius:50%"></i>www.keelbyhomestay.com</li></ul>
  <div class="brand-small"><span class="mark"></span>Keelby Homestay</div>
  <p class="addr">www.keelbyhomestay.com<span>(555) 246-8130</span></p>
  <div class="stamp"></div>
  <div class="line" style="top:174px"></div>
  <div class="line" style="top:203px"></div>
  <div class="line" style="top:233px"></div>
</section>

</body>
</html>
```